Logo and Packaging for Low Dose Full Spectrum Cannabis Extract Capsules - Marlowe Co

Hi! I am hoping to get a logo and packaging design for low dose (2, 5, and 10mg) full spectrum cannabis extract capsules.

Overall we are going for a natural, healthy, earthy. clean, safe, trustworthy, environmentally friendly look and would love to use lots of natural colors like brown and green as well as white.

For the Marlowe Co logo I would love to have something clean and simple, possibly involving a stylized capsule or plant/leaf.

The labels will be printed on 8x2" (203.2 x 50.8 mm) paper bands that will wrap around the 3.125" (79.4 mm) wide fronts and backs of white tin containers -the sides are 0.5625” (14.3 mm). There will be a 0.5" (12.7 mm) of overlap at the end of the band that will be covered by the adhesive.

Designs should include the following information:

Front:
- Marlowe Co logo (not the main focus)
- X mg THC per capsule (final versions with 2, 5, and 10 and this should be relatively prominent. The capsules get darker as they get to higher strengths and it might be nice to represent that on the labels as well)
- Indica, Sativa, or Hybrid (maybe Purple for Indica, Green for Sativa, and a third color for Hybrid?)
- 15 Full Spectrum Cannabis Extract Capsules

Back:
- For adult use only. Keep away from children.
- This product has not been analyzed or evaluated by the QVR
- Ingredients: Olive oil, full spectrum cannabis extract, gelatin capsules
- Made in DC

Wealthy young professionals between 25 and 55, especially women, for the woman who has it all as a discreet and classy alternative to sleep aids, other herbal supplements, or a glass of Pinot noir

Serif
Sans Serif
• Garamond, Lucida Bright, Georgia, Goudy, Bangkok, Brooklyn, Sage

```html
<!DOCTYPE html>
<html lang="en">
<head>
<meta charset="utf-8">
<title>Marlowe Co — Logo and Capsule Packaging</title>
<link href="https://fonts.googleapis.com/css2?family=Sorts+Mill+Goudy&family=Damion&family=Roboto:wght@500;700&family=Oswald:wght@500;600&display=swap" rel="stylesheet">
<style>
  :root {
    --brown: #6b4428;
    --forest: #0b5a2d;
    --leaf: #0f8c40;
    --indica: #45254f;
    --hybrid: #e3891c;
    --rule: #dd8a1f;
    --face: #f2f2f2;
    --page: #ffffff;
  }
  * { box-sizing: border-box; margin: 0; padding: 0; }
  html, body { width: 720px; height: 1200px; overflow: hidden; background: var(--page); }
  .canvas { position: relative; width: 720px; height: 1200px; }

  .brand-mark {
    position: absolute; top: 130px; left: 0; width: 720px;
    display: flex; justify-content: center; align-items: center; gap: 18px;
  }
  .brand-mark__dot { width: 26px; height: 26px; border-radius: 50%; background: var(--forest); }
  .brand-mark__name {
    font-family: "Sorts Mill Goudy", Georgia, serif;
    font-size: 60px; color: var(--forest); line-height: 1;
  }

  .divider { position: absolute; top: 372px; left: 102px; width: 516px; height: 2px; background: var(--rule); }

  .pack {
    position: absolute; width: 138px; height: 214px; background: var(--face);
    text-align: center; --tone: var(--forest); --ink: var(--forest);
  }
  .pack--indica { --tone: var(--indica); --ink: var(--indica); }
  .pack--sativa { --tone: var(--forest); --ink: var(--leaf); }
  .pack--hybrid { --tone: var(--hybrid); --ink: var(--hybrid); }

  .pack__brand {
    position: absolute; top: 10px; left: 0; width: 100%;
    font-family: "Sorts Mill Goudy", Georgia, serif; font-size: 25px; color: var(--brown); line-height: 1;
  }
  .pack__strain {
    position: absolute; top: 58px; left: 0; width: 100%;
    font-family: "Damion", cursive; font-size: 30px; color: var(--tone); line-height: 1;
  }
  .pack__band {
    position: absolute; left: 0; width: 100%; background: var(--tone); color: #fff;
    font-family: "Roboto", Arial, sans-serif; font-weight: 500;
    display: flex; flex-direction: column; justify-content: center;
  }
  .pack__band--dose { top: 135px; height: 23px; font-size: 11px; }
  .pack__band--warning { top: 137px; height: 34px; font-size: 9.5px; line-height: 1.3; }

  .pack__count {
    position: absolute; top: 163px; left: 0; width: 100%;
    font-family: "Oswald", Arial, sans-serif; font-weight: 600; font-size: 19px; color: var(--brown); line-height: 1;
  }
  .pack__contents {
    position: absolute; top: 185px; left: 0; width: 100%;
    font-family: "Oswald", Arial, sans-serif; font-weight: 500; font-size: 11px; color: var(--ink); line-height: 1;
  }

  .pack__fine {
    position: absolute; top: 175px; left: 4px; right: 4px; text-align: left;
    font-family: "Oswald", Arial, sans-serif; font-weight: 500; font-size: 4.6px; line-height: 1.35; color: var(--brown);
  }
  .pack__fine .pack__ingredients { color: var(--ink); margin-top: 2px; }
  .pack__origin {
    position: absolute; top: 196px; left: 0; width: 100%;
    font-family: "Oswald", Arial, sans-serif; font-weight: 500; font-size: 10px; color: var(--ink); line-height: 1;
  }
</style>
</head>
<body>
<main class="canvas">
  <header class="brand-mark">
    <span class="brand-mark__dot"></span>
    <span class="brand-mark__name">Marlowe Co</span>
  </header>

  <div class="divider"></div>

  <section class="pack-row pack-row--front">
    <article class="pack pack--indica" style="left:91px; top:489px;">
      <div class="pack__brand">Marlowe Co</div>
      <div class="pack__strain">Indica</div>
      <div class="pack__band pack__band--dose">2 mg THC per capsule</div>
      <div class="pack__count">15 Full Spectrum</div>
      <div class="pack__contents">Cannabis Extract Capsules</div>
    </article>
    <article class="pack pack--sativa" style="left:277px; top:489px;">
      <div class="pack__brand">Marlowe Co</div>
      <div class="pack__strain">Sativa</div>
      <div class="pack__band pack__band--dose">5 mg THC per capsule</div>
      <div class="pack__count">15 Full Spectrum</div>
      <div class="pack__contents">Cannabis Extract Capsules</div>
    </article>
    <article class="pack pack--hybrid" style="left:460px; top:489px;">
      <div class="pack__brand">Marlowe Co</div>
      <div class="pack__strain">Hybrid</div>
      <div class="pack__band pack__band--dose">10 mg THC per capsule</div>
      <div class="pack__count">15 Full Spectrum</div>
      <div class="pack__contents">Cannabis Extract Capsules</div>
    </article>
  </section>

  <section class="pack-row pack-row--back">
    <article class="pack pack--indica" style="left:91px; top:840px;">
      <div class="pack__brand">Marlowe Co</div>
      <div class="pack__strain">Indica</div>
      <div class="pack__band pack__band--warning"><span>For adult use only.</span><span>Keep away from children.</span></div>
      <div class="pack__fine">
        <p>This product has not been analyzed or evaluated by the QVR</p>
        <p class="pack__ingredients">Ingredients:<br>Olive oil, full spectrum cannabis extract, gelatin capsules</p>
      </div>
      <div class="pack__origin">Made in DC</div>
    </article>
    <article class="pack pack--sativa" style="left:277px; top:840px;">
      <div class="pack__brand">Marlowe Co</div>
      <div class="pack__strain">Sativa</div>
      <div class="pack__band pack__band--warning"><span>For adult use only.</span><span>Keep away from children.</span></div>
      <div class="pack__fine">
        <p>This product has not been analyzed or evaluated by the QVR</p>
        <p class="pack__ingredients">Ingredients:<br>Olive oil, full spectrum cannabis extract, gelatin capsules</p>
      </div>
      <div class="pack__origin">Made in DC</div>
    </article>
    <article class="pack pack--hybrid" style="left:460px; top:840px;">
      <div class="pack__brand">Marlowe Co</div>
      <div class="pack__strain">Hybrid</div>
      <div class="pack__band pack__band--warning"><span>For adult use only.</span><span>Keep away from children.</span></div>
      <div class="pack__fine">
        <p>This product has not been analyzed or evaluated by the QVR</p>
        <p class="pack__ingredients">Ingredients:<br>Olive oil, full spectrum cannabis extract, gelatin capsules</p>
      </div>
      <div class="pack__origin">Made in DC</div>
    </article>
  </section>
</main>
</body>
</html>
```